Acai Bowl and Coffee Van need new Menus

We currently have a basic menu that is displayed in an A3 frame. It lacks images, specifically of the Acai Bowls and is difficult to read and understand.

We need a new Acai Bowl Menu and a new Drink Menu but in a more attractive and easier to read format.
We would like images of the Acai Bowls (using Images supplied or make your own) in order to show customers what is on each bowl. Customers chose what granola they would like from the three that are available. Currently we tell customers to check the bottom of the menu as they are often unaware they get to chose.

The drink menu items are simple (we have removed smoothies from our menu entirely).
The drink menu needs to have "Chai Latte" and "Dirty Chai Latte" added as options with the same S,M,L pricing as a Latte.

I have attached images of the menus and a photo of how the menus are displayed on The Brindle Cart. Also attached is photos of the Acai Bowls and other food / drink items on the menu if you wish to use them in your design. I have included the files for all of our logo variations.

Our main objective with the menu redesign is to have the menu more appealing and easier to read and understand.

Industry/Entity Type

Food and Coffee

Font styles to use
Other font styles liked:
• Orplid Pro (Fill and Shadow), Trend Sans One

Colors

Designer to choose colors to be used in the design.

Requirements
Must have
• The final design must include prices and be editable in the case of any price changes in the future.

```html
<!DOCTYPE html>
<html lang="en">
<head>
<meta charset="utf-8">
<title>The Brindle Cart – Menus</title>
<link href="https://fonts.googleapis.com/css2?family=Josefin+Sans:wght@400;600;700&display=swap" rel="stylesheet">
<style>
:root{
  --bg:#eeeded;
  --sage:#d9e0d6;
  --white:#ffffff;
  --pink:#efdfe2;
  --tan:#b39c7f;
  --tan-dark:#8f7a60;
  --ink:#1b1a18;
}
*{margin:0;padding:0;box-sizing:border-box}
html,body{width:1200px;height:1200px;overflow:hidden;background:var(--bg)}
body{position:relative;font-family:"Josefin Sans",sans-serif;color:var(--ink);text-transform:uppercase}
.menu{position:absolute;top:222px;width:535px;height:755px}
.drinks{left:44px;background:var(--sage)}
.acai{left:619px;background:var(--white)}
.abs{position:absolute}
.title{position:absolute;left:34px;font-family:"Josefin Sans",sans-serif;font-weight:700;font-size:78px;line-height:1;letter-spacing:0;color:var(--white);-webkit-text-stroke:1.4px var(--tan-dark);text-shadow:4px 4px 0 var(--tan-dark);white-space:nowrap}
.acai .title{left:28px;-webkit-text-stroke:1.4px var(--tan);text-shadow:4px 4px 0 var(--tan)}
.c-ced{position:relative;display:inline-block}
.ced{position:absolute;left:50%;bottom:-14px;width:12px;height:16px;margin-left:-6px;border:3px solid var(--tan);border-top:none;border-left:none;border-radius:0 0 10px 0;-webkit-text-stroke:0;text-shadow:none}
.heading{font-size:13px;font-weight:600;letter-spacing:2px;line-height:1;white-space:nowrap}
.label{position:absolute;font-size:6.5px;letter-spacing:1.2px;color:var(--tan-dark);top:4px}
.row{position:relative;height:12.5px;font-size:8.4px;font-weight:600;letter-spacing:1.4px;line-height:12.5px;white-space:nowrap}
.price{position:absolute;top:1.5px;width:36px;height:10px;background:var(--white);font-size:8.4px;line-height:11px;text-align:center;letter-spacing:1px;font-weight:600}
.sub{font-size:6.6px;letter-spacing:1.2px;color:var(--tan-dark);line-height:9px}
.section .items{margin-top:14px}
.milk{height:24px}
.milk .row{height:10px;line-height:10px}
.milk .price{width:42px;top:0}
.badge{position:absolute;border-radius:50%;display:flex;flex-direction:column;align-items:center;justify-content:center;text-align:center}
.save{left:381px;top:476px;width:86px;height:86px;background:var(--white);color:var(--tan-dark);transform:rotate(8deg);line-height:1.1}
.step{position:absolute;width:34px;height:34px;border-radius:50%;background:var(--tan);color:var(--white);font-size:22px;font-weight:400;text-align:center;line-height:38px;border:1.5px solid var(--white);box-shadow:0 0 0 1px var(--tan)}
.box{position:absolute;background:var(--pink);border-radius:8px}
.gran-name{position:absolute;left:14px;font-size:9px;font-weight:600;letter-spacing:1.4px}
.gran-desc{position:absolute;left:14px;font-size:6.3px;letter-spacing:1px;color:var(--tan-dark);line-height:9px;width:270px}
.bowl{position:absolute;width:215px;height:81px}
.bowl h3{position:absolute;top:8px;left:0;font-size:13px;font-weight:600;letter-spacing:2px;white-space:nowrap}
.bowl h3.long{font-size:12px;letter-spacing:1.2px}
.bowl .tag{position:absolute;top:8px;width:41px;height:11px;background:var(--tan);color:var(--white);font-size:7.6px;line-height:12px;text-align:center;border-radius:2px;letter-spacing:1px}
.bowl .what{position:absolute;top:27px;left:0;font-size:8px;font-weight:600;letter-spacing:1.2px;line-height:11px;white-space:nowrap}
.bowl .note{position:absolute;top:51px;left:0;font-size:6.3px;letter-spacing:1px;line-height:9px;color:var(--tan-dark);white-space:nowrap}
.vline{position:absolute;border-left:1px dashed #cdb9b9}
.hline{position:absolute;border-top:1px dashed #cdb9b9}
.tops{position:absolute;top:12px;font-size:7.4px;font-weight:600;letter-spacing:1px;line-height:9.7px;list-style:none;white-space:nowrap}
.pill{position:absolute;top:728px;width:40px;height:11px;background:var(--tan);color:var(--white);font-size:7.6px;line-height:12px;text-align:center;border-radius:2px;letter-spacing:1px;margin-left:-20px}
.brand{position:absolute;left:0;width:1200px;top:1086px;display:flex;justify-content:center;align-items:center;gap:10px;font-size:14px;font-weight:600;letter-spacing:3px;color:var(--tan-dark)}
.brand-dot{width:14px;height:14px;border-radius:50%;background:var(--tan)}
</style>
</head>
<body>

<section class="menu drinks">
  <h1 class="title" style="top:38px">DRINKS</h1>
  <h1 class="title" style="top:114px">MENU</h1>

  <div class="section abs" style="left:36px;top:212px;width:250px">
    <h2 class="heading">Coffee</h2>
    <span class="label" style="left:116px">Small</span><span class="label" style="left:162px">Reg</span><span class="label" style="left:206px">Large</span>
    <div class="items">
      <div class="row">Cappuccino<span class="price" style="left:110px">5.50</span><span class="price" style="left:156px">6.50</span><span class="price" style="left:201px">7.50</span></div>
      <div class="row">Latte<span class="price" style="left:110px">5.50</span><span class="price" style="left:156px">6.50</span><span class="price" style="left:201px">7.50</span></div>
      <div class="row">Flat White<span class="price" style="left:110px">5.50</span><span class="price" style="left:156px">6.50</span><span class="price" style="left:201px">7.50</span></div>
      <div class="row">Espresso<span class="price" style="left:110px">4.00</span><span class="price" style="left:156px">4.50</span><span class="price" style="left:201px">5.00</span></div>
      <div class="row">Long Black<span class="price" style="left:110px">4.50</span><span class="price" style="left:156px">5.00</span><span class="price" style="left:201px">5.50</span></div>
      <div class="row">Macchiato<span class="price" style="left:156px">5.50</span><span class="price" style="left:201px">6.00</span></div>
    </div>
  </div>

  <div class="section abs" style="left:36px;top:343px;width:250px">
    <h2 class="heading">Chocolate</h2>
    <span class="label" style="left:116px">Small</span><span class="label" style="left:162px">Reg.</span><span class="label" style="left:206px">Large</span>
    <div class="items">
      <div class="row">Mocha<span class="price" style="left:110px">5.50</span><span class="price" style="left:156px">6.50</span><span class="price" style="left:201px">7.50</span></div>
      <div class="row">Hot Chocolate<span class="price" style="left:110px">5.00</span><span class="price" style="left:156px">6.00</span><span class="price" style="left:201px">7.00</span></div>
    </div>
  </div>

  <div class="section abs" style="left:36px;top:423px;width:250px">
    <h2 class="heading">Chai Latte</h2>
    <span class="label" style="left:116px">Small</span><span class="label" style="left:162px">Reg.</span><span class="label" style="left:206px">Large</span>
    <div class="items">
      <div class="row">Chai Latte<span class="price" style="left:110px">5.50</span><span class="price" style="left:156px">6.50</span><span class="price" style="left:201px">7.50</span></div>
      <div class="row">Dirty Chai Latte<span class="price" style="left:110px">5.50</span><span class="price" style="left:156px">6.50</span><span class="price" style="left:201px">7.50</span></div>
    </div>
  </div>

  <div class="section abs" style="left:36px;top:502px;width:250px">
    <h2 class="heading">Cold Beverages</h2>
    <span class="label" style="left:162px">Reg.</span><span class="label" style="left:206px">Large</span>
    <div class="items">
      <div class="row">Cold Brew Coffee<span class="price" style="left:156px">6.50</span><span class="price" style="left:201px">8.50</span></div>
      <div class="row">Iced Coffee<span class="price" style="left:156px">6.50</span><span class="price" style="left:201px">7.50</span></div>
      <div class="row">Iced Mocha<span class="price" style="left:156px">6.50</span><span class="price" style="left:201px">7.50</span></div>
      <div class="row">Iced Long Black<span class="price" style="left:156px">5.50</span><span class="price" style="left:201px">6.50</span></div>
      <div class="row">Iced Chocolate<span class="price" style="left:156px">6.50</span><span class="price" style="left:201px">7.50</span></div>
      <div class="row">Iced Pure Tea<span class="price" style="left:156px">5.00</span><span class="price" style="left:201px">6.00</span></div>
      <p class="sub">Lemongrass and ginger |<br>White tea, acai and coconut | Chai</p>
    </div>
  </div>

  <div class="section abs" style="left:36px;top:651px;width:250px">
    <h2 class="heading">More Beverages</h2>
    <div class="items">
      <div class="row">Tonic Kombucha<span class="price" style="left:110px">4.50</span></div>
      <div class="row">Bottled Water<span class="price" style="left:110px">3.00</span></div>
    </div>
  </div>

  <div class="section abs" style="left:324px;top:211px;width:180px">
    <h2 class="heading">Extras</h2>
    <div class="items">
      <div class="row">Additional Shot<span class="price" style="left:130px">0.50</span></div>
      <div class="row">Shot of Syrup<span class="price" style="left:130px">0.50</span></div>
      <p class="sub">Vanilla | Caramel | Hazelnut</p>
    </div>
  </div>

  <div class="section abs" style="left:324px;top:342px;width:190px">
    <h2 class="heading">Alternative Milks</h2>
    <div class="items">
      <div class="milk"><div class="row">Oat Milk<span class="price" style="left:134px">+ 0.70</span></div><p class="sub">Oatfield Dairy Co</p></div>
      <div class="milk"><div class="row">Almond Milk<span class="price" style="left:134px">+ 0.70</span></div><p class="sub">Nut Works</p></div>
      <div class="milk"><div class="row">Soy Milk<span class="price" style="left:134px">+ 0.70</span></div><p class="sub">Sunny Soy Co</p></div>
      <div class="milk"><div class="row">Lactose Free<span class="price" style="left:134px">+ 0.70</span></div><p class="sub">Nut Works</p></div>
    </div>
  </div>

  <div class="badge save">
    <span style="font-size:6px;letter-spacing:1px">Save</span>
    <span style="font-size:10px;letter-spacing:1.5px">50 cents</span>
    <span style="font-size:5.5px;letter-spacing:1px">with your own</span>
    <span style="font-size:9px;letter-spacing:1.5px">Reusable<br>cup</span>
  </div>

  <div class="section abs" style="left:324px;top:599px;width:180px">
    <h2 class="heading">Pure Tea</h2>
    <span class="label" style="left:136px">Reg.</span>
    <div class="items">
      <div class="row">English Breakfast<span class="price" style="left:130px">4.00</span></div>
      <div class="row">Morning Dew<span class="price" style="left:130px">4.00</span></div>
      <div class="row">Gunpowder Green<span class="price" style="left:130px">4.00</span></div>
      <div class="row">Chai Tea<span class="price" style="left:130px">4.00</span></div>
      <div class="row">Peppermint<span class="price" style="left:130px">4.00</span></div>
      <div class="row">Cocoa &amp; Peppermint<span class="price" style="left:130px">4.00</span></div>
    </div>
  </div>
</section>

<section class="menu acai">
  <h1 class="title" style="top:38px" aria-label="Açai">A<span class="c-ced">C<span class="ced"></span></span>AI</h1>
  <h1 class="title" style="top:114px">BOWLS</h1>

  <div class="step" style="left:22px;top:203px">1</div>
  <h2 class="heading abs" style="left:67px;top:210px">Açai Base</h2>

  <div class="badge" style="left:91px;top:260px;width:86px;height:86px;background:var(--pink);color:var(--tan-dark);transform:rotate(10deg)">
    <span style="font-size:6.5px;letter-spacing:1px;line-height:1.2">We use Shoreline<br>Crunch granola:</span>
    <span style="font-size:4.5px;letter-spacing:.6px;line-height:7px;margin-top:2px">Vegan friendly<br>No refined sugars<br>Dairy free<br>Gluten free</span>
  </div>
  <svg class="abs" style="left:164px;top:304px" width="52" height="32" viewBox="0 0 52 32">
    <path d="M2 28 Q24 30 44 8" fill="none" stroke="var(--tan)" stroke-width="1" stroke-dasharray="2 2"/>
    <path d="M40 6 L47 3 L45 11 Z" fill="var(--tan)"/>
  </svg>

  <div class="box" style="left:218px;top:225px;width:292px;height:124px">
    <span class="gran-name" style="top:7px">Gingernut Crunch</span>
    <p class="gran-desc" style="top:17px">Inspired by beloved ginger nut biscuits, this granola brings the warmth and comfort of ginger, nutmeg, and cinnamon to your favourite bowl.</p>
    <span class="gran-name" style="top:54px">Toasted Almond &amp; Cinnamon</span>
    <p class="gran-desc" style="top:64px">Combines the warmth of cinnamon with toasted Aussie almonds and 100% WA grown lupin flakes.</p>
    <span class="gran-name" style="top:93px">Cacao, Hazelnut &amp; Chia</span>
    <p class="gran-desc" style="top:103px">One for the chocolate lovers, tastes like a crunchy version of hazelnut spread with hazelnuts and cacao.</p>
  </div>
  <div class="step" style="left:201px;top:203px">2</div>
  <h2 class="heading abs" style="left:245px;top:211px">Pick your ♥-granola</h2>

  <div class="box" style="left:39px;top:376px;width:471px;height:248px">
    <div class="vline" style="left:230px;top:8px;height:232px"></div>
    <div class="hline" style="left:8px;top:80px;width:455px"></div>
    <div class="hline" style="left:8px;top:164px;width:455px"></div>

    <div class="bowl" style="left:17px;top:0">
      <h3>Original Bowl</h3><span class="tag" style="left:154px">$ 17.50</span>
      <p class="what">Coconut flakes and fresh<br>seasonal fruit</p>
      <p class="note">A basic bowl, great for you to<br>start your own creation</p>
    </div>
    <div class="bowl" style="left:250px;top:0">
      <h3>Tropical Bowl</h3><span class="tag" style="left:168px">$ 18.50</span>
      <p class="what">Shredded coconut, passionfruit,<br>mango and pineapple</p>
      <p class="note">Make it extra refreshing by adding<br>some kiwifruit for $1.00</p>
    </div>
    <div class="bowl" style="left:17px;top:80px">
      <h3>Berry Bowl</h3><span class="tag" style="left:154px">$ 18.50</span>
      <p class="what">Shredded coconut. Goji berries.<br>Strawberry and blueberry</p>
      <p class="note">Add some cacao nibs for an<br>extra $1.00</p>
    </div>
    <div class="bowl" style="left:250px;top:80px">
      <h3>Choc Bowl</h3><span class="tag" style="left:168px">$20.50</span>
      <p class="what">Shredded coconut, cacao nibs,<br>banana, strawberry and Hazelnova</p>
      <p class="note">We recommend the 'cacao, hazelnut<br>&amp; chia granola' with this one</p>
    </div>
    <div class="bowl" style="left:17px;top:162px">
      <h3>Spekkel Bowl</h3><span class="tag" style="left:154px">$ 21.00</span>
      <p class="what">Banana, shredded coconut,<br>goji berries, Spekkel spread<br>and crumble</p>
      <p class="note" style="top:62px">If you love peanut butter, you<br>will love this bowl too</p>
    </div>
    <div class="bowl" style="left:250px;top:162px">
      <h3 class="long">Brindle Favourite</h3><span class="tag" style="left:172px">$ 21.00</span>
      <p class="what">Coconut flakes, goji beries,<br>chia seeds, banana, strawberry<br>and peanut butter</p>
      <p class="note" style="top:62px">Add a peanut butter protein slice<br>on top for $ 2.50</p>
    </div>
  </div>
  <div class="step" style="left:21px;top:352px">3</div>
  <h2 class="heading abs" style="left:65px;top:360px">Pick your ♥-topping combo</h2>

  <div class="box" style="left:39px;top:652px;width:471px;height:75px">
    <div class="vline" style="left:132px;top:6px;height:64px;border-left-style:dotted"></div>
    <div class="vline" style="left:239px;top:6px;height:64px;border-left-style:dotted"></div>
    <div class="vline" style="left:352px;top:6px;height:64px;border-left-style:dotted"></div>
    <ul class="tops" style="left:12px"><li>• Chia seeds</li><li>• Passionfruit</li><li>• Buckini</li><li>• Coconut flakes</li><li>• Shredded coconut</li></ul>
    <ul class="tops" style="left:138px"><li>• Goji berries</li><li>• Cacao nibs</li><li>• Honey</li><li>• Dates</li><li>• Extra fruit</li><li>• Extra granola</li></ul>
    <ul class="tops" style="left:246px"><li>• Peanut butter</li><li>• Almond butter</li><li>• Hazelnova</li><li>• Spekkel</li></ul>
    <ul class="tops" style="left:358px"><li>• Shoreline Crunch</li><li>&nbsp;&nbsp;Peanut butter</li><li>&nbsp;&nbsp;protein slice</li></ul>
  </div>
  <div class="step" style="left:22px;top:629px">4</div>
  <h2 class="heading abs" style="left:67px;top:637px">Additional toppings</h2>
  <span class="pill" style="left:103px">$ 0.50</span>
  <span class="pill" style="left:223px">$ 1.00</span>
  <span class="pill" style="left:341px">$ 2.00</span>
  <span class="pill" style="left:452px">$ 2.50</span>
</section>

<div class="brand"><span class="brand-dot"></span><span>The Brindle Cart</span></div>

</body>
</html>
```